Velnimo.org
Brackwater Residents association
plz star rating....
in the back of the card it should have the following
K&T BULKWARE SUPPLIERS
847 HAZELMOOR ROAD
OLVERTON MA. 02946
we will like the back ground of the card to be red... our colors are red yellow and blue.

```html
<!DOCTYPE html>
<html lang="en">
<head>
<meta charset="utf-8">
<title>Velnimo.org – Business Card</title>
<link href="https://fonts.googleapis.com/css2?family=Open+Sans:wght@400;600;700&display=swap" rel="stylesheet">
<style>
  :root {
    --backdrop: #e9e6e1;
    --card: #c8202b;
    --brand-blue: #1f7fc4;
    --brand-yellow: #f5c518;
    --ink: #ffffff;
    --ink-soft: #fbe3e4;
  }
  * { box-sizing: border-box; margin: 0; padding: 0; }
  html, body {
    width: 1200px; height: 408px; overflow: hidden;
    background: var(--backdrop);
    font-family: "Open Sans", Arial, sans-serif;
    color: var(--ink);
  }
  .stage { position: relative; width: 1200px; height: 408px; }
  .card {
    position: absolute; top: 58px;
    width: 506px; height: 284px;
    background: var(--card);
    box-shadow: 0 3px 10px rgba(0,0,0,0.25);
  }
  .card--front { left: 62px; }
  .card--back { left: 640px; }

  .brand { display: flex; flex-direction: column; }
  .brand__name {
    display: flex; align-items: center; gap: 8px;
    font-weight: 700; font-size: 34px; line-height: 1;
    color: var(--brand-yellow); letter-spacing: -0.5px;
  }
  .brand__mark { width: 14px; height: 14px; background: var(--brand-blue); }
  .brand__tagline {
    margin-top: 4px;
    font-weight: 700; font-size: 13px; color: var(--ink);
  }

  .card--front .brand { position: absolute; left: 26px; top: 30px; }
  .address {
    position: absolute; left: 26px; top: 132px;
    font-style: normal;
    font-size: 11px; line-height: 16px; color: var(--ink-soft);
  }
  .contact {
    position: absolute; left: 26px; top: 188px;
    font-size: 11px; line-height: 16.5px; color: var(--ink-soft);
    list-style: none;
  }
  .holder { position: absolute; right: 52px; top: 206px; }
  .holder__name { font-size: 15px; font-weight: 600; color: var(--ink); }
  .holder__title { margin-top: 4px; font-size: 11px; color: var(--ink-soft); }

  .card--back .brand {
    position: absolute; left: 0; right: 0; top: 52px; align-items: center;
  }
  .slogan {
    position: absolute; left: 0; right: 0; top: 130px; text-align: center;
    font-size: 16px; font-weight: 700; color: var(--brand-yellow); letter-spacing: 0.5px;
  }
  .supplier {
    position: absolute; left: 0; right: 0; top: 170px; text-align: center;
    font-style: normal;
    font-size: 11px; line-height: 17px; color: var(--ink); letter-spacing: 0.6px;
  }
  .supplier__name { font-weight: 700; font-size: 12px; }
  .website {
    position: absolute; left: 0; right: 0; bottom: 22px; text-align: center;
    font-size: 10px; color: var(--ink-soft);
  }
</style>
</head>
<body>
<main class="stage">
  <section class="card card--front" aria-label="Card front">
    <div class="brand">
      <div class="brand__name"><span class="brand__mark"></span>Velnimo.org</div>
      <div class="brand__tagline">Brackwater Residents Association</div>
    </div>
    <address class="address">
      58 Fennick Street<br>
      Olverton, Ma 02946
    </address>
    <ul class="contact">
      <li>P : 555-213-4470</li>
      <li>F : 555-214-8832</li>
      <li>E : velnimo2006@mailbox.com</li>
      <li>W: www.velnimo.org</li>
    </ul>
    <div class="holder">
      <div class="holder__name">Dario Quintellan</div>
      <div class="holder__title">President</div>
    </div>
  </section>

  <section class="card card--back" aria-label="Card back">
    <div class="brand">
      <div class="brand__name"><span class="brand__mark"></span>Velnimo.org</div>
      <div class="brand__tagline">Brackwater Residents Association</div>
    </div>
    <p class="slogan">we buy properties</p>
    <address class="supplier">
      <span class="supplier__name">K&amp;T BULKWARE SUPPLIERS</span><br>
      847 HAZELMOOR ROAD<br>
      OLVERTON MA. 02946
    </address>
    <p class="website">www.velnimo.org</p>
  </section>
</main>
</body>
</html>
```